Bright Path Medical Centers - website

Would like a multicultural website with pictures of physicians and nurses of all races interacting with patients of all races and ages from kids to seniors (in a medical practice) not a hospital.

Would like a page devoted to Pediatric Care, Adult/Family Care, Retirees/Senior Care. With a list of general primary care services for each page, including lab and transportation.
Updates

Target Market(s)

Adult medicine, Pediatric Medicine, Retiree/Senior Care

Industry/Entity Type

Health Care

Number of Pages Required

3 page

Font styles to use
Sans Serif

Requirements
Must have
• I like the website “oakridgefamilyclinic.example” in Atlanta.
• Prefer the design look and feel like this even though the services are very different.

```html
<!DOCTYPE html>
<html lang="en">
<head>
<meta charset="utf-8">
<title>Bright Path Medical Centers</title>
<link rel="stylesheet" href="https://fonts.googleapis.com/css2?family=Lato:ital,wght@0,400;0,700;0,900;1,700&display=swap">
<style>
  :root {
    --teal: #22a8bc;
    --teal-soft: #7fd0da;
    --orange: #f57c00;
    --ink: #3a3a3a;
    --band: #f1f1f1;
    --white: #ffffff;
    --dark: #1d1d1d;
    --footer-text: #d8d8d8;
    --hero-a: #9aa7b0;
    --hero-b: #5c6d78;
  }
  * { box-sizing: border-box; margin: 0; padding: 0; }
  html, body { width: 1200px; height: 3046px; overflow: hidden; }
  body { position: relative; background: var(--white); font-family: "Lato", sans-serif; color: var(--ink); }
  .abs { position: absolute; }

  /* Header + hero */
  .hero { left: 0; top: 0; width: 1200px; height: 680px; background: linear-gradient(120deg, var(--hero-a), var(--hero-b) 55%, #7b8c98); }
  .topbar { left: 0; top: 0; width: 1200px; height: 96px; background: rgba(40,40,40,.55); }
  .brand { left: 77px; top: 31px; width: 300px; white-space: nowrap; font-family: "Lato", sans-serif; font-weight: 900; font-size: 24px; line-height: 32px; color: var(--white); text-transform: uppercase; letter-spacing: 0; }
  .nav a { position: absolute; top: 28px; height: 37px; line-height: 37px; font-size: 12px; font-weight: 700; color: var(--white); text-decoration: none; text-transform: uppercase; white-space: nowrap; }
  .nav a.active { background: var(--teal); border-radius: 19px; padding: 0 22px; }
  .hero-title { left: 0; top: 296px; width: 1200px; text-align: center; color: var(--white); font-weight: 700; font-size: 54px; line-height: 58px; text-transform: uppercase; }
  .dots { left: 565px; top: 643px; display: flex; gap: 8px; }
  .dots span { width: 10px; height: 10px; border-radius: 50%; background: var(--white); }
  .dots span.on { background: var(--orange); }
  .hero-wave { left: 0; top: 590px; }

  /* Section text */
  .h2 { font-weight: 700; font-size: 28px; color: var(--teal); text-transform: uppercase; }
  .copy { font-size: 15px; line-height: 26px; color: var(--ink); }
  .btn { display: block; height: 53px; line-height: 53px; width: 207px; text-align: center; background: var(--orange); color: var(--white); font-weight: 700; font-size: 16px; border-radius: 27px; text-transform: uppercase; text-decoration: none; }

  .about-title { left: 0; top: 736px; width: 1200px; text-align: center; }
  .about-copy { left: 120px; top: 780px; width: 960px; text-align: center; }
  .about-btn { left: 497px; top: 926px; }

  .band { left: 0; }
  .photo-circle { border-radius: 50%; border: 5px solid var(--teal-soft); }
  .service-title { font-size: 26px; }
  .service-copy { width: 580px; }

  /* Blog */
  .blog-title { left: 0; top: 2240px; width: 1200px; text-align: center; }
  .card { top: 2304px; width: 331px; }
  .card .thumb { width: 331px; height: 193px; border-radius: 12px; }
  .card h3 { margin-top: 16px; font-size: 17px; font-weight: 900; color: var(--teal); text-transform: uppercase; }
  .card p { margin-top: 4px; font-size: 15px; line-height: 22px; }
  .card .more { display: block; margin-top: 10px; font-size: 14px; font-weight: 700; font-style: italic; color: var(--orange); text-decoration: none; }

  /* Footer */
  .footer-bg { left: 0; top: 2690px; }
  .sub-title { left: 0; top: 2738px; width: 1200px; text-align: center; font-size: 22px; }
  .sub-copy { left: 0; top: 2780px; width: 1200px; text-align: center; font-size: 14px; color: var(--footer-text); }
  .sub-form { left: 343px; top: 2815px; width: 513px; height: 46px; background: var(--white); border-radius: 23px; }
  .sub-form .label { position: absolute; left: 46px; top: 0; line-height: 46px; font-size: 14px; color: #333; }
  .sub-form .mail { position: absolute; left: 18px; top: 16px; }
  .sub-form .send { position: absolute; right: 3px; top: 3px; width: 66px; height: 40px; border-radius: 20px; background: var(--orange); }
  .foot-nav { left: 0; top: 2908px; width: 1200px; text-align: center; }
  .foot-nav a { display: inline-block; margin: 0 10px; font-size: 11px; font-weight: 700; color: var(--white); text-decoration: none; text-transform: uppercase; }
  .copyright { left: 0; top: 2940px; width: 1200px; text-align: center; font-size: 11px; color: var(--footer-text); }
  .social { left: 502px; top: 2978px; display: flex; gap: 22px; }
  .social span { width: 22px; height: 22px; border-radius: 50%; background: #cfcfcf; }
</style>
</head>
<body>

  <!-- Hero -->
  <div class="abs hero" role="img" aria-label="Photo of a physician reviewing paperwork with a senior patient at a clinic desk"></div>
  <svg class="abs hero-wave" width="1200" height="100" viewBox="0 0 1200 100">
    <path d="M0 45 C300 95 600 100 850 80 C1000 68 1120 48 1200 40 L1200 100 L0 100 Z" fill="var(--white)"/>
  </svg>
  <div class="abs topbar"></div>
  <div class="abs brand">Bright Path Medical</div>
  <nav class="nav">
    <a class="active" style="left:406px">Home</a>
    <a style="left:495px">About Us</a>
    <a style="left:587px">Paediatric Care</a>
    <a style="left:723px">Adult/Family Care</a>
    <a style="left:875px">Retirees/Senior Care</a>
    <a style="left:1050px">Contact Us</a>
  </nav>
  <h1 class="abs hero-title">Bright Path<br>Medical Centers</h1>
  <div class="abs dots"><span class="on"></span><span></span><span></span><span></span></div>

  <!-- About -->
  <h2 class="abs h2 about-title">About Bright Path Medical Centers</h2>
  <p class="abs copy about-copy">Aliquam molestie, mi et imperdiet euismod, dui purus auctor tellus, et interdum lacus lectus et ante. Sed accumsan sollicitudin sapien, sit amet adipiscing turpis gravida ac. In congue, neque ac lobortis volutpat, libero mauris varius mi, vitae suscipit ipsum ligula vitae risus. Duis aliquam nibh a dui iaculis viverra id a velit. Vivamus egestas risus in magna varius commodo.<br>Sed semper viverra egestas.</p>
  <a class="abs btn about-btn">Read More</a>

  <!-- Paediatric -->
  <svg class="abs band" style="top:1070px" width="1200" height="340" viewBox="0 0 1200 340">
    <path d="M0 18 C250 -5 500 10 700 22 C900 34 1080 10 1200 4 L1200 312 C1000 330 800 300 600 310 C380 322 180 340 0 322 Z" fill="var(--band)"/>
  </svg>
  <div class="abs photo-circle" style="left:105px;top:1023px;width:370px;height:370px;background:linear-gradient(135deg,#d7e3ec,#b9cbd8);" role="img" aria-label="Photo of a smiling doctor with a young child patient"></div>
  <h2 class="abs h2 service-title" style="left:524px;top:1138px">Paediatric Care</h2>
  <p class="abs copy service-copy" style="left:524px;top:1182px">Aliquam molestie, mi et imperdiet euismod, dui purus auctor tellus, et interdum lacus lectus et ante. Sed accumsan sollicitudin sapien, sit amet adipiscing turpis gravida ac. In congue, neque ac lobortis volutpat, libero mauris varius mi, vitae suscipit ipsum ligula vitae risus.</p>
  <a class="abs btn" style="left:524px;top:1303px">Read More</a>

  <!-- Adult / Family -->
  <svg class="abs band" style="top:1455px" width="1200" height="360" viewBox="0 0 1200 360">
    <path d="M0 24 C200 4 420 20 640 30 C860 40 1060 20 1200 8 L1200 340 C1000 350 760 330 560 330 C340 330 160 352 0 345 Z" fill="var(--band)"/>
  </svg>
  <div class="abs photo-circle" style="left:710px;top:1413px;width:370px;height:370px;background:linear-gradient(135deg,#f0e6dc,#d9c6b3);" role="img" aria-label="Photo of a doctor standing in front of a multigenerational family"></div>
  <h2 class="abs h2 service-title" style="left:75px;top:1517px">Adult/Family Care</h2>
  <p class="abs copy service-copy" style="left:75px;top:1561px">Aliquam molestie, mi et imperdiet euismod, dui purus auctor tellus, et interdum lacus lectus et ante. Sed accumsan sollicitudin sapien, sit amet adipiscing turpis gravida ac. In congue, neque ac lobortis volutpat, libero mauris varius mi, vitae suscipit ipsum ligula vitae risus.</p>
  <a class="abs btn" style="left:75px;top:1683px">Read More</a>

  <!-- Retirees / Senior -->
  <svg class="abs band" style="top:1845px" width="1200" height="360" viewBox="0 0 1200 360">
    <path d="M0 20 C220 2 460 18 680 28 C900 38 1080 18 1200 10 L1200 348 C1000 340 780 318 560 322 C340 326 160 345 0 340 Z" fill="var(--band)"/>
  </svg>
  <div class="abs photo-circle" style="left:105px;top:1796px;width:370px;height:370px;background:linear-gradient(135deg,#bfe0d8,#5a6e8a);" role="img" aria-label="Photo of a nurse helping a senior woman walk with a frame"></div>
  <h2 class="abs h2 service-title" style="left:524px;top:1912px">Retirees/Senior Care</h2>
  <p class="abs copy service-copy" style="left:524px;top:1956px">Aliquam molestie, mi et imperdiet euismod, dui purus auctor tellus, et interdum lacus lectus et ante. Sed accumsan sollicitudin sapien, sit amet adipiscing turpis gravida ac. In congue, neque ac lobortis volutpat, libero mauris varius mi, vitae suscipit ipsum ligula vitae risus.</p>
  <a class="abs btn" style="left:524px;top:2077px">Read More</a>

  <!-- Blog -->
  <h2 class="abs h2 blog-title">Blog Posts</h2>
  <article class="abs card" style="left:75px">
    <div class="thumb" style="background:linear-gradient(135deg,#cfe3f0,#6f98b8);" role="img" aria-label="Photo of doctors consulting with a patient in a bright clinic"></div>
    <h3>Vestibulum ante ipsum primis</h3>
    <p>Aliquam molestie, mi et imperdiet euismod, dui purus auctor tellus, et interdum lacus lectus et ante vel ornare..</p>
    <a class="more">Continue Reading</a>
  </article>
  <article class="abs card" style="left:434px">
    <div class="thumb" style="background:linear-gradient(135deg,#d8c8b8,#3a4f8a);" role="img" aria-label="Photo of a nurse checking a senior patient's blood pressure"></div>
    <h3>Vestibulum ante ipsum primis</h3>
    <p>Aliquam molestie, mi et imperdiet euismod, dui purus auctor tellus, et interdum lacus lectus et ante vel ornare..</p>
    <a class="more">Continue Reading</a>
  </article>
  <article class="abs card" style="left:796px">
    <div class="thumb" style="background:linear-gradient(135deg,#f3ede6,#e2d2c6);" role="img" aria-label="Photo of a doctor listening to a young girl's heartbeat"></div>
    <h3>Vestibulum ante ipsum primis</h3>
    <p>Aliquam molestie, mi et imperdiet euismod, dui purus auctor tellus, et interdum lacus lectus et ante vel ornare..</p>
    <a class="more">Continue Reading</a>
  </article>

  <!-- Footer -->
  <svg class="abs footer-bg" width="1200" height="356" viewBox="0 0 1200 356">
    <path d="M0 30 C300 0 700 -4 1200 22 L1200 356 L0 356 Z" fill="var(--dark)"/>
  </svg>
  <h2 class="abs h2 sub-title">Email Subscribe</h2>
  <p class="abs sub-copy">Vestibulum ante ipsum primis in faucibus orci luctus et ultrices posuere cubilia</p>
  <div class="abs sub-form">
    <svg class="mail" width="16" height="13" viewBox="0 0 16 13"><rect x="1" y="1" width="14" height="11" rx="1.5" fill="none" stroke="#333" stroke-width="1.4"/><path d="M1.5 2 L8 7.5 L14.5 2" fill="none" stroke="#333" stroke-width="1.4"/></svg>
    <span class="label">Enter Email Address</span>
    <span class="send">
      <svg width="66" height="40" viewBox="0 0 66 40"><path d="M24 20 L42 12 L36 29 L32 23 Z" fill="var(--white)"/></svg>
    </span>
  </div>
  <nav class="abs foot-nav">
    <a>Home</a><a>About Us</a><a>Paediatric Care</a><a>Adult/Family Care</a><a>Retirees/Senior Care</a><a>Contact Us</a>
  </nav>
  <p class="abs copyright">Copyright © 2017, Company Name. All Right Reserved</p>
  <div class="abs social"><span></span><span></span><span></span><span></span><span></span></div>

</body>
</html>
```